Novu Staffing Tri Fold Brochure

My company is a recruiting/staffing firm. I need a design that is going to be professional, bright, young, hip and fun. Pictures are key! We want people working in an office, packaging, food production and/or light industrial environment. Must embrace DIVERSITY. Please use the 4 primary colors from the Novu Logo to accent the piece, but not too busy. I am including the content that I would like to be included in the trifold as well as a sample of a trifold I have used in the past in addition to a couple of logos. My website is www.NovuStaffing.example for look and feel.

Target Market(s)

Logistics, Distribution and Manufacturing companies

Industry/Entity Type

Staffing

Requirements
Must have
• Clean, colorful, eye catching, great pictures and graphics. Photo's of diverse people working, in a office, or production setting.
Nice to have
• Must be professional
Should not have
• Not too busy.

```html
<!DOCTYPE html>
<html lang="en">
<head>
<meta charset="utf-8">
<title>Novu Staffing Tri-Fold Brochure</title>
<link rel="stylesheet" href="https://fonts.googleapis.com/css2?family=Oswald:wght@500;600&family=Roboto:wght@300;400;500;700&display=swap">
<style>
  :root {
    --backdrop: #6d6d6d;
    --paper: #ffffff;
    --red: #d7141b;
    --red-dark: #b10d12;
    --yellow: #f6cb14;
    --navy: #2c2a6e;
    --ink: #111111;
    --photo-warm: #a58a6c;
    --photo-cool: #8a8f9c;
  }
  * { margin: 0; padding: 0; box-sizing: border-box; }
  html, body { width: 900px; height: 1200px; overflow: hidden; }
  body {
    background: var(--backdrop);
    font-family: "Roboto", Arial, sans-serif;
    color: var(--ink);
    position: relative;
  }
  .brochure {
    position: absolute;
    left: 21px; top: 270px;
    width: 858px; height: 660px;
    background: var(--paper);
    display: flex;
    box-shadow: 0 6px 18px rgba(0,0,0,.35);
  }
  .panel { position: relative; width: 286px; height: 660px; overflow: hidden; }

  .photo { position: absolute; }

  /* Left panel */
  .panel--about .photo-production {
    left: 0; top: 0; width: 286px; height: 209px;
    background: linear-gradient(135deg, #c9c4bd 0%, var(--photo-warm) 55%, #6f5a44 100%);
  }
  .definition-bar {
    position: absolute; left: 0; top: 205px; width: 248px; height: 35px;
    background: var(--navy); color: #fff;
    font-family: "Oswald", "Arial Narrow", sans-serif; font-weight: 500;
    font-size: 17px; line-height: 35px; padding-left: 14px; letter-spacing: .2px;
  }
  .definition-term {
    position: absolute; left: 0; top: 252px; width: 286px; text-align: center;
    font-size: 13px; font-weight: 500;
  }
  .definition-quote {
    position: absolute; left: 22px; top: 276px; width: 242px; text-align: center;
    font-size: 11px; line-height: 14px;
  }
  .mission-label {
    position: absolute; left: 91px; top: 322px; width: 96px; height: 32px;
    background: var(--yellow); color: var(--ink);
    font-family: "Oswald", "Arial Narrow", sans-serif; font-weight: 500;
    font-size: 17px; line-height: 32px; text-align: center;
  }
  .mission-text {
    position: absolute; left: 26px; top: 370px; width: 234px; text-align: center;
    font-size: 11px; line-height: 14px;
  }
  .panel--about .photo-team {
    left: 0; top: 420px; width: 286px; height: 148px;
    background: linear-gradient(180deg, #f3f3f3 0%, #d9d6d3 40%, #4a4a55 100%);
  }
  .phone-bar {
    position: absolute; left: 0; top: 568px; width: 286px; height: 48px;
    background: var(--red); color: #fff; text-align: center;
    font-size: 23px; font-weight: 300; line-height: 48px;
  }
  .phone-bar b, .phone b { font-weight: 700; }
  .site {
    position: absolute; left: 0; width: 286px; text-align: center;
    font-size: 12px; font-weight: 500; letter-spacing: 2px;
  }
  .panel--about .site { top: 630px; color: var(--ink); }

  /* Middle panel */
  .panel--contact {
    background: linear-gradient(90deg, #f4f4f4 0%, #ffffff 12%, #ffffff 82%, #e3e3e3 100%);
  }
  .panel--contact .photo-office {
    left: 0; top: 0; width: 286px; height: 220px;
    background: linear-gradient(180deg, rgba(140,145,160,.55) 0%, rgba(180,180,190,.4) 55%, rgba(255,255,255,0) 100%);
  }
  .contact-label {
    position: absolute; left: 58px; top: 205px; width: 176px; height: 26px;
    background: var(--red); color: #fff; text-align: center;
    font-family: "Oswald", "Arial Narrow", sans-serif; font-weight: 500;
    font-size: 16px; line-height: 26px;
  }
  .region {
    position: absolute; left: 0; width: 286px; text-align: center;
  }
  .region h3 {
    font-size: 18px; font-weight: 500; color: var(--navy); line-height: 24px;
  }
  .region p { font-size: 14px; line-height: 22px; }

  /* Right panel */
  .brand {
    position: absolute; left: 0; top: 26px; width: 286px;
    display: flex; align-items: center; justify-content: center; gap: 10px;
  }
  .brand-dot { width: 16px; height: 16px; border-radius: 50%; background: var(--red); }
  .brand-name {
    font-family: "Roboto", Arial, sans-serif; font-weight: 500;
    font-size: 34px; color: var(--navy); letter-spacing: .5px;
  }
  .cover-band {
    position: absolute; left: 0; top: 193px; width: 286px; height: 298px;
    background: linear-gradient(90deg, var(--red-dark) 0%, var(--red) 18%);
  }
  .cover-photo-frame {
    position: absolute; left: 14px; top: 126px; width: 258px; height: 243px;
    background: #fff; padding: 4px;
    box-shadow: 0 2px 6px rgba(0,0,0,.3);
  }
  .cover-photo-frame .photo {
    position: static; width: 100%; height: 100%;
    background: linear-gradient(160deg, #b8a58f 0%, #8c7a68 45%, #2d2c36 100%);
  }
  .cover-copy {
    position: absolute; left: 0; top: 392px; width: 286px; text-align: center; color: #fff;
  }
  .cover-copy .lead { font-size: 14px; line-height: 18px; }
  .cover-copy .headline-1 {
    font-family: "Oswald", "Arial Narrow", sans-serif; font-weight: 500;
    font-size: 21px; line-height: 26px; letter-spacing: .3px;
  }
  .cover-copy .headline-2 {
    font-family: "Oswald", "Arial Narrow", sans-serif; font-weight: 600;
    font-size: 34px; line-height: 40px; letter-spacing: .5px;
  }
  .tagline {
    position: absolute; left: 0; top: 496px; width: 286px; height: 63px;
    background: var(--yellow); text-align: center;
    display: flex; align-items: center; justify-content: center;
    font-size: 14px; line-height: 18px; padding: 0 30px;
  }
  .phone {
    position: absolute; left: 0; top: 574px; width: 286px; text-align: center;
    font-size: 24px; font-weight: 300; color: var(--navy);
  }
  .site-bar {
    position: absolute; left: 0; top: 620px; width: 286px; height: 40px;
    background: var(--navy);
  }
  .panel--cover .site { top: 633px; color: #fff; }
</style>
</head>
<body>
  <main class="brochure">
    <section class="panel panel--about">
      <div class="photo photo-production" role="img" aria-label="Photo: worker in gloves tending a food production line of baked goods"></div>
      <h2 class="definition-bar">DEFINITION OF NOVU – VERB</h2>
      <p class="definition-term">To be in harmony or accord; To Fit; Agree</p>
      <p class="definition-quote">“Yes the candidate meets the requirements, yeah they have the skills, but do they Novu?”</p>
      <h2 class="mission-label">MISSION</h2>
      <p class="mission-text">At NOVU Staffing, we are passionate in our pursuit to change lives by connecting great people with great organizations.</p>
      <div class="photo photo-team" role="img" aria-label="Photo: diverse team of smiling professionals standing together"></div>
      <div class="phone-bar">+1 555-<b>010</b>-4570</div>
      <p class="site">www.novustaffing.example</p>
    </section>

    <section class="panel panel--contact">
      <div class="photo photo-office" role="img" aria-label="Faded photo: colleagues working together at a laptop in an office"></div>
      <h2 class="contact-label">CONTACT US</h2>
      <div class="region" style="top:246px">
        <h3>GEORGIA</h3>
        <p>Cartersville – 555-010-8348</p>
        <p>Marietta – 555-010-9731</p>
        <p>Savannah – 555-010-6838</p>
        <p>Union City – 555-010-0735</p>
      </div>
      <div class="region" style="top:388px">
        <h3>INDIANA</h3>
        <p>Plainfield – 555-010-8558</p>
      </div>
      <div class="region" style="top:460px">
        <h3>PENNSYLVANIA</h3>
        <p>Harrisburg – 555-010-3700</p>
        <p>Bethlehem – 555-010-6799</p>
      </div>
      <div class="region" style="top:554px">
        <h3>TEXAS</h3>
        <p>Arlington – 555-010-4570</p>
      </div>
    </section>

    <section class="panel panel--cover">
      <div class="brand">
        <span class="brand-dot"></span>
        <span class="brand-name">Novu Staffing</span>
      </div>
      <div class="cover-band"></div>
      <div class="cover-photo-frame">
        <div class="photo" role="img" aria-label="Photo: confident diverse group of young professionals in business attire"></div>
      </div>
      <div class="cover-copy">
        <p class="lead">Take the first step</p>
        <p class="headline-1">TOWARD A BETTER</p>
        <p class="headline-2">OPPORTUNITY</p>
      </div>
      <p class="tagline">At Novu Staffing, we are interested in improving lives.</p>
      <p class="phone">+1 555-<b>010</b>-4570</p>
      <div class="site-bar"></div>
      <p class="site">www.novustaffing.example</p>
    </section>
  </main>
</body>
</html>
```